JMT - Business Card Design Project

We need a business card based on our logo
Updates

Hi I just upload logo file in AI format Thanks and regards

Target Market(s)

Bank, Big companies, Business owners

Industry/Entity Type

Business

Font styles to use
Sans Serif

```html
<!DOCTYPE html>
<html lang="fr">
<head>
<meta charset="utf-8">
<title>JMT – Carte de visite</title>
<link rel="stylesheet" href="https://fonts.googleapis.com/css2?family=Questrial&family=Montserrat:wght@700&display=swap">
<style>
  :root {
    --backdrop: #e4e6ea;
    --paper: #fbfbfa;
    --navy: #2c3b63;
    --navy-deep: #1f2b4c;
    --silver: #a9b1b1;
    --ink-soft: #7d8688;
    --white: #ffffff;
  }
  * { margin: 0; padding: 0; box-sizing: border-box; }
  html, body {
    width: 1200px;
    height: 800px;
    overflow: hidden;
    background: var(--backdrop);
  }
  .canvas {
    position: relative;
    width: 1200px;
    height: 800px;
  }
  .business-card {
    position: absolute;
    left: 150px;
    top: 140px;
    width: 900px;
    height: 520px;
    background: var(--paper);
    overflow: hidden;
    box-shadow: 0 18px 40px rgba(20, 28, 50, 0.18);
    font-family: "Questrial", "Century Gothic", sans-serif;
  }
  .card-shapes {
    position: absolute;
    inset: 0;
    width: 100%;
    height: 100%;
  }
  .brand {
    position: absolute;
    left: 80px;
    top: 52px;
    color: var(--navy);
  }
  .brand-mark {
    display: block;
    font-size: 124px;
    line-height: 1;
    letter-spacing: 2px;
  }
  .brand-name {
    display: block;
    font-size: 29px;
    margin-top: 4px;
  }
  .brand-tagline {
    display: block;
    font-size: 14px;
    color: var(--ink-soft);
    margin-top: 4px;
    letter-spacing: 0.3px;
  }
  .holder {
    position: absolute;
    right: 56px;
    top: 64px;
    text-align: right;
    color: var(--white);
  }
  .holder-name {
    font-family: "Montserrat", "Century Gothic", sans-serif;
    font-weight: 700;
    font-size: 32px;
    line-height: 1.1;
  }
  .holder-role {
    font-size: 26px;
    line-height: 1.2;
  }
  .contact-list {
    position: absolute;
    left: 330px;
    top: 320px;
    list-style: none;
    color: var(--white);
    font-size: 25px;
  }
  .contact-item {
    display: flex;
    align-items: center;
    height: 36px;
  }
  .contact-icon {
    width: 22px;
    height: 22px;
    margin-right: 14px;
    flex: none;
  }
  .contact-item strong { font-weight: 700; font-family: "Montserrat", "Century Gothic", sans-serif; font-size: 23px; }
</style>
</head>
<body>
<main class="canvas">
  <article class="business-card">
    <svg class="card-shapes" viewBox="0 0 900 520" preserveAspectRatio="none" aria-hidden="true">
      <defs>
        <linearGradient id="navyShade" x1="0" y1="0" x2="1" y2="1">
          <stop offset="0" stop-color="var(--navy)"/>
          <stop offset="1" stop-color="var(--navy-deep)"/>
        </linearGradient>
      </defs>
      <path class="silver-band" fill="var(--silver)" d="M0,288 C260,272 520,205 688,0 L702,0 C522,232 252,304 0,332 Z"/>
      <path class="navy-field" fill="url(#navyShade)" d="M0,330 C252,302 522,230 700,0 L900,0 L900,520 L0,520 Z"/>
    </svg>

    <header class="brand">
      <span class="brand-mark">JMT</span>
      <span class="brand-name">Cabinet Marlot &amp; Associés</span>
      <span class="brand-tagline">Expertise-comptable • Audit • Conseil</span>
    </header>

    <div class="holder">
      <p class="holder-name">Elise Fournel</p>
      <p class="holder-role">Directeur</p>
    </div>

    <ul class="contact-list">
      <li class="contact-item">
        <svg class="contact-icon" viewBox="0 0 24 24" aria-hidden="true"><path fill="var(--white)" d="M6.6 10.8a15.1 15.1 0 0 0 6.6 6.6l2.2-2.2a1 1 0 0 1 1-.25 11.4 11.4 0 0 0 3.6.6 1 1 0 0 1 1 1V20a1 1 0 0 1-1 1A17 17 0 0 1 3 4a1 1 0 0 1 1-1h3.5a1 1 0 0 1 1 1c0 1.25.2 2.45.6 3.6a1 1 0 0 1-.25 1z"/></svg>
        01.45.72.19.38
      </li>
      <li class="contact-item">
        <svg class="contact-icon" viewBox="0 0 24 24" aria-hidden="true"><rect x="2" y="5" width="20" height="14" fill="var(--white)"/><path d="M2 5l10 8 10-8" fill="none" stroke="var(--navy)" stroke-width="2"/></svg>
        elise@<strong>jmtassocies</strong>.com
      </li>
      <li class="contact-item">
        <svg class="contact-icon" viewBox="0 0 24 24" aria-hidden="true"><circle cx="12" cy="12" r="9.5" fill="none" stroke="var(--white)" stroke-width="2"/><path d="M2.5 12h19M12 2.5c-3 3-3 16 0 19M12 2.5c3 3 3 16 0 19" fill="none" stroke="var(--white)" stroke-width="1.6"/></svg>
        www.<strong>jmtassocies</strong>.com
      </li>
      <li class="contact-item">
        <svg class="contact-icon" viewBox="0 0 24 24" aria-hidden="true"><circle cx="12" cy="12" r="9" fill="var(--white)"/></svg>
        Elise_JMT
      </li>
      <li class="contact-item">
        <svg class="contact-icon" viewBox="0 0 24 24" aria-hidden="true"><rect x="3" y="3" width="18" height="18" fill="var(--white)"/></svg>
        elisefournel
      </li>
    </ul>
  </article>
</main>
</body>
</html>
```